Hello Creative Minds!
Our business is after a elegant and classy flyer that draws attention!
The business is Tallow Brook - Lawn Rejuvenation Services. We provide services that maintain a healthy and vibrant green lawn through the tough Australian seasons. The products we use limits the water needed to keep grass green to a minimum - practically none at all! This not only helps the home owner or home seller but the environment by limiting the use of water that is needed to create a green lawn. The products we use are made from natural ingredients that are and pet friendly.
This fly will be our introductory offer to the market. Below are the required points that need to be on the flyer. Attached is the business logo, before & after pictures and 1 example of the LAYOUT not DESIGN of what the flyer should be laid out like or similar to. Feel free to use different 'Lawn Mower' pictures.
All the best; if you need any questions answered please feel free to message.
REQUIRED POINTS (Please re-phrase were possible);
*Instantly restores the natural green colour of grass – year round
*Lasts for up to 3 months
*Substantially reduces watering needs
*Pet friendly
*Stays green during droughts and water restrictions
*UV fade resistant
*Won’t bleed, run, or stain once absorbed into the grass
*Safe for the environment, pets and people
*Works in extreme heat, cold and frost
*Organic and natural – no harmful chemicals
*Reduces the amount of fertilizer
and water used on lawns
*Kerb appeal is essential for getting your property sold for the highest price possible
SERVICES & PRICING
Lawn maintenance (cut & trim) starting from $60
Lawn rejuvenation starting from $80 (Only $27 a month for 3 months)*
Package deal starting from $120
Introductory offer: 25% off all services. Refer a friend, when they book you receive another 25% off your next service.
LOCATIONS
Nowra to Sydney
CONTACT NUMBER
Will be posted with the winner - please leave an area for this.
SOCIAL MEDIA
Please add Facebook and Instagram logo's
Updates
Competition has finished, thank you to all that have participated! I will review and comment on the flyers that need assistance. All the best with future designs!
Target Market(s)
home owners, home sellers, property developers, real estates and nursing homes and government housing.
Industry/Entity Type
Lawn Care
Look and feel

```html
<!DOCTYPE html>
<html lang="en">
<head>
<meta charset="utf-8">
<title>Tallow Brook – Lawn Rejuvenation Services Flyer</title>
<link href="https://fonts.googleapis.com/css2?family=Yellowtail&family=Montserrat:wght@600;700;800&family=Lato:wght@400;700&display=swap" rel="stylesheet">
<style>
  :root {
    --backdrop: #e4e4e2;
    --navy: #1d2631;
    --lime: #d6e04a;
    --green: #7fb23a;
    --leaf: #8fc043;
    --white: #ffffff;
    --soft: #e9ecef;
    --red: #d7242b;
    --frame: #c9ced3;
    --straw: #b89c63;
    --turf: #4f8f2e;
  }
  * { box-sizing: border-box; margin: 0; padding: 0; }
  html, body { width: 1200px; height: 869px; overflow: hidden; background: var(--backdrop); }
  .flyer {
    position: absolute; left: 307px; top: 20px;
    width: 586px; height: 829px;
    background: var(--navy);
    font-family: "Lato", sans-serif; color: var(--soft);
    overflow: hidden;
  }
  .headline {
    position: absolute; font-family: "Yellowtail", cursive; font-weight: 400;
    background: linear-gradient(90deg, var(--lime), var(--green));
    -webkit-background-clip: text; background-clip: text; color: transparent;
    filter: drop-shadow(2px 3px 2px rgba(0,0,0,.55));
    line-height: 1; white-space: nowrap; z-index: 5;
  }
  .headline--one { left: 36px; top: 42px; font-size: 78px; transform: rotate(-4deg); }
  .headline--two { left: 200px; top: 112px; font-size: 78px; transform: rotate(-4deg); }

  .photo-panel {
    position: absolute; left: 132px; top: 140px; width: 336px; height: 352px;
    border: 1.5px solid var(--frame); padding: 6px;
  }
  .photo { width: 100%; height: 164px; }
  .photo--before { background: linear-gradient(180deg, #8a8d90 0%, #8a8d90 35%, #b8c36a 55%, #9a9da0 100%); }
  .photo--after { margin-top: 8px; background: linear-gradient(180deg, #7c8084 0%, #7c8084 35%, #55a034 55%, #8e9194 100%); }

  .badge { position: absolute; width: 150px; height: 150px; z-index: 4; }
  .badge--before { left: 48px; top: 118px; }
  .badge--after { left: 364px; top: 226px; }
  .badge-label { font-family: "Montserrat", sans-serif; font-weight: 700; font-size: 11px; letter-spacing: 3px; fill: var(--white); }
  .badge-note {
    position: absolute; left: 390px; top: 280px; width: 100px; z-index: 6;
    font-family: "Montserrat", sans-serif; font-weight: 800; font-size: 12.5px; line-height: 1.15;
    color: var(--white); text-align: center; text-shadow: 1px 1px 2px rgba(0,0,0,.8);
  }

  .offer {
    position: absolute; left: 40px; top: 268px; width: 212px; height: 100px; z-index: 6;
    transform: rotate(-2deg);
  }
  .offer svg { position: absolute; inset: 0; }
  .offer-text { position: absolute; inset: 0; text-align: center; color: var(--white); font-family: "Montserrat", sans-serif; font-weight: 700; padding-top: 6px; padding-right: 10px; }
  .offer-kicker { font-size: 12px; }
  .offer-amount { font-size: 27px; font-weight: 800; line-height: 1; }
  .offer-scope { font-size: 13px; line-height: 1.1; }
  .offer-refer { font-size: 7.5px; margin-top: 5px; line-height: 1.3; }

  .box { position: absolute; border: 1.2px solid var(--soft); }
  .box-title {
    position: absolute; top: -8px; background: var(--navy); padding: 0 5px;
    font-family: "Montserrat", sans-serif; font-weight: 700; font-size: 11px; color: var(--white);
  }
  .benefits { left: 60px; top: 526px; width: 312px; height: 152px; }
  .benefits .box-title { left: 100px; }
  .benefit-cols { display: flex; gap: 10px; padding: 14px 8px 0 12px; }
  .benefit-list { list-style: none; flex: 1; }
  .benefit-list li { position: relative; padding-left: 9px; font-size: 7.6px; line-height: 1.25; margin-bottom: 4px; }
  .benefit-list li::before { content: "✓"; position: absolute; left: 0; color: var(--lime); font-weight: 700; }

  .pricing { left: 387px; top: 518px; width: 162px; height: 152px; }
  .pricing .box-title { left: 16px; }
  .price-list { padding: 14px 10px 0 12px; }
  .price-name { font-family: "Montserrat", sans-serif; font-weight: 700; font-size: 9px; color: var(--lime); }
  .price-from { font-size: 8px; margin: 2px 0 8px; }
  .price-from strong { font-size: 11.5px; color: var(--white); }

  .brand { position: absolute; left: 120px; top: 700px; width: 240px; text-align: center; font-family: "Montserrat", sans-serif; font-weight: 700; color: var(--leaf); }
  .brand-name { display: flex; align-items: center; justify-content: center; gap: 8px; font-size: 30px; line-height: 1; }
  .brand-dot { width: 14px; height: 14px; border-radius: 50%; background: var(--leaf); }
  .brand-tag { font-size: 8px; letter-spacing: 2.6px; margin-top: 6px; }

  .call { position: absolute; left: 98px; top: 782px; font-family: "Montserrat", sans-serif; font-weight: 800; font-size: 16px; color: var(--white); white-space: nowrap; }
  .call-number { font-size: 23px; color: var(--leaf); margin-left: 6px; }

  .contacts { position: absolute; left: 418px; top: 692px; list-style: none; }
  .contacts li { display: flex; align-items: center; gap: 8px; font-size: 8.2px; height: 22px; margin-bottom: 8px; }
  .contact-icon { width: 22px; height: 22px; background: linear-gradient(135deg, var(--lime), var(--green)); display: flex; align-items: center; justify-content: center; border-radius: 2px; }
</style>
</head>
<body>
<main class="flyer">
  <h1 class="headline headline--one">Make your lawn</h1>
  <p class="headline headline--two">great again!</p>

  <div class="photo-panel">
    <div class="photo photo--before" role="img" aria-label="Backyard before treatment: dry patchy lawn beside a concrete patio and grey fence"></div>
    <div class="photo photo--after" role="img" aria-label="Same backyard after treatment: vibrant green lawn beside the patio"></div>
  </div>

  <svg class="badge badge--before" viewBox="0 0 150 150">
    <defs><path id="arcBefore" d="M 22 100 A 56 56 0 0 1 98 22"/></defs>
    <circle cx="77" cy="77" r="58" fill="var(--straw)" stroke="var(--white)" stroke-width="2" role="img" aria-label="Close-up of dry, straw-coloured grass"/>
    <text class="badge-label"><textPath href="#arcBefore" startOffset="0">BEFORE</textPath></text>
  </svg>

  <svg class="badge badge--after" viewBox="0 0 150 150">
    <defs><path id="arcAfter" d="M 80 10 A 66 66 0 0 1 146 76"/></defs>
    <circle cx="75" cy="77" r="58" fill="var(--turf)" stroke="var(--white)" stroke-width="2" role="img" aria-label="Close-up of lush green grass"/>
    <text class="badge-label"><textPath href="#arcAfter" startOffset="4">AFTER</textPath></text>
  </svg>
  <p class="badge-note">LASTS<br>FOR UP TO<br>3 MONTHS</p>

  <div class="offer">
    <svg viewBox="0 0 212 100" preserveAspectRatio="none">
      <polygon points="0,0 198,0 212,50 198,100 0,100" fill="var(--red)" stroke="var(--white)" stroke-width="1"/>
    </svg>
    <div class="offer-text">
      <div class="offer-kicker">INTRODUCTORY OFFER:</div>
      <div class="offer-amount">25% OFF</div>
      <div class="offer-scope">ALL SERVICES</div>
      <div class="offer-refer">REFER A FRIEND: When they book, you<br>will receive 25% OFF your next service!</div>
    </div>
  </div>

  <section class="box benefits">
    <h2 class="box-title">DIRECT BENEFITS</h2>
    <div class="benefit-cols">
      <ul class="benefit-list">
        <li>Instantly restores the natural green colour of grass – year round</li>
        <li>Substantially reduces watering needs</li>
        <li>Pet friendly</li>
        <li>Stays green during droughts and water restrictions</li>
        <li>Organic and natural – no harmful chemicals</li>
        <li>Won't bleed, run, or stain once absorbed into the grass</li>
      </ul>
      <ul class="benefit-list">
        <li>Safe for the environment, pets and people</li>
        <li>Works in extreme heat, cold and frost</li>
        <li>UV fade resistant</li>
        <li>Reduces the amount of fertilizer and water used on lawns</li>
        <li>Kerb appeal is essential for getting your property sold for the highest price possible</li>
      </ul>
    </div>
  </section>

  <section class="box pricing">
    <h2 class="box-title">SERVICES &amp; PRICING</h2>
    <div class="price-list">
      <div class="price-name">LAWN MAINTENANCE</div>
      <div class="price-from">Starting from <strong>$60</strong></div>
      <div class="price-name">LAWN REJUVENATION</div>
      <div class="price-from">Starting from <strong>$80</strong></div>
      <div class="price-name">PACKAGE DEAL</div>
      <div class="price-from">Starting from <strong>$120</strong></div>
      <div class="price-name">LOCATIONS</div>
      <div class="price-from">Nowra to Sydney</div>
    </div>
  </section>

  <div class="brand">
    <div class="brand-name"><span class="brand-dot"></span>Tallow Brook</div>
    <div class="brand-tag">LAWN REJUVENATION SERVICES</div>
  </div>

  <p class="call">CALL TODAY <span class="call-number">0412 738 590</span></p>

  <ul class="contacts">
    <li><span class="contact-icon"><svg width="14" height="10" viewBox="0 0 14 10"><rect x="0.5" y="0.5" width="13" height="9" fill="none" stroke="var(--navy)" stroke-width="1.2"/><polyline points="0.5,0.5 7,6 13.5,0.5" fill="none" stroke="var(--navy)" stroke-width="1.2"/></svg></span>hello@tallowbrooklawns.com.au</li>
    <li><span class="contact-icon"></span>@tallowbrooklawns</li>
    <li><span class="contact-icon"></span>@tallowbrooklawns</li>
  </ul>
</main>
</body>
</html>
```